Lanternis in a league of it's own

Lanternis is a pan European contact center.
We serve our clients in 18 languages from Antwerp in Belgium, Fez in Morocco and with our partner Velomreach.
We have a presentation and we would like to make it much more visible;
Less text, more images or animation.
Our business case is based on three elements with three colours :
blue sky : because we ar fully organized in the cloud,
Green : in our customer care college, out green village we put a lot of energy in training,
Orange : when technology is good and people have a good knowledge, passion will come...
Eventually we are ready to payfor some stock images - to negotiate-
For answers to your questions : tomas.verlaek@quillnet.be

```html
<!DOCTYPE html>
<html lang="en">
<head>
<meta charset="utf-8">
<title>Lanternis – presentation slides</title>
<link href="https://fonts.googleapis.com/css2?family=Roboto:wght@300;400;500&display=swap" rel="stylesheet">
<style>
  :root{
    --sky:#0d96d4;
    --leaf:#8cc040;
    --flame:#e9572f;
    --navy:#232b3c;
    --ink:#4a4f5a;
    --muted:#9a9ea6;
    --paper:#ffffff;
    --backdrop:#cbcccf;
  }
  *{margin:0;padding:0;box-sizing:border-box}
  html,body{width:1200px;height:900px;overflow:hidden;background:var(--backdrop)}
  body{font-family:"Roboto",Arial,sans-serif;font-weight:300}
  .stage{position:absolute;left:0;top:0;width:1500px;height:1125px;transform:scale(.8);transform-origin:0 0}
  .slide{position:absolute;width:446px;height:345px;background:var(--paper);overflow:hidden}
  .slide-title{position:absolute;left:17px;top:16px;font-size:16px;color:var(--sky);font-weight:300;letter-spacing:-.2px}
  .title-rule{position:absolute;left:17px;top:35px;width:412px;height:2px;
    background:linear-gradient(90deg,var(--flame) 0 33%,var(--leaf) 33% 66%,var(--sky) 66% 100%)}
  .slide-footer{position:absolute;left:0;bottom:0;width:100%;height:8px;background:var(--navy)}
  .page-no{position:absolute;right:4px;bottom:0;font-size:5px;color:#fff;line-height:8px}
  .brand{position:absolute;display:flex;align-items:center;gap:3px;font-weight:500;color:var(--navy)}
  .brand .dot{border-radius:50%;background:var(--sky)}
  .brand-small{left:9px;bottom:17px;font-size:10px}
  .brand-small .dot{width:11px;height:11px}
  .chart{position:absolute;left:0;top:0}
  .year{font-size:11px;fill:var(--sky);font-family:"Roboto",Arial,sans-serif;font-weight:300}
  .legend{position:absolute;top:265px;width:95px}
  .legend-head{display:flex;align-items:center;gap:3px;font-size:6.5px;color:var(--ink)}
  .legend-head i{display:block;width:6px;height:6px}
  .legend p{font-size:4px;line-height:5.5px;color:var(--ink);text-align:justify;margin-top:2px;padding-left:9px}
  .stat{position:absolute;top:95px;width:112px;text-align:center}
  .stat svg{display:block;margin:0 auto}
  .stat-value{margin-top:21px;font-size:13px;color:var(--sky)}
  .stat p{margin-top:4px;font-size:5.5px;line-height:8.5px;color:var(--muted)}
  .col{position:absolute;top:62px;width:177px}
  .col p{position:relative;font-size:7.6px;line-height:15.8px;color:#7c8089;text-align:justify;text-align-last:left;padding-left:0}
  .col p + p{margin-top:15px}
  .col p::before{content:"";position:absolute;left:-9px;top:5px;width:5px;height:5px;border-radius:50%;background:var(--leaf)}
  .dark{background:var(--navy)}
  .panel-title{position:absolute;left:18px;top:16px;font-size:14px;color:#fff;font-weight:300}
  .panel-sub{position:absolute;left:24px;top:122px;font-size:9.5px;color:#fff;font-weight:400}
  .panel-text{position:absolute;left:24px;top:138px;width:176px;font-size:7.6px;line-height:15.8px;color:#b9bdc6;text-align:justify;text-align-last:left}
  .brand-light{color:#fff}
  .photo-portrait{position:absolute;left:220px;top:0;width:226px;height:345px;
    background:linear-gradient(160deg,#f2f2f2 0%,#d9d9d9 45%,#8e8e8e 100%)}
  .photo-team{position:absolute;inset:0;background:radial-gradient(ellipse at 50% 60%,#56627c 0%,#3c4760 55%,#2c3548 100%)}
  .section{position:absolute;left:0;top:155px;width:100%;text-align:center}
  .section svg{display:block;margin:0 auto}
  .section-rule{width:128px;height:1px;background:var(--sky);margin:10px auto 0}
  .section-title{margin-top:6px;font-size:14px;color:var(--sky);font-weight:300}
  .brand-large{left:38px;top:30px;font-size:30px;gap:8px;font-weight:400}
  .brand-large .dot{width:36px;height:36px}
  .map{position:absolute;left:0;top:105px;width:446px;height:128px;
    background:linear-gradient(135deg,#dcd8cf 0%,#e8e4dc 50%,#d3d0c8 100%)}
  .contact{position:absolute;left:0;top:233px;width:446px;height:110px;background:var(--navy)}
  .contact-item{position:absolute;display:flex;gap:6px;font-size:7px;line-height:9px;color:#fff}
  .contact-item .ico{flex:none;width:10px;height:10px;border-radius:50%;background:#fff;position:relative;top:-1px}
  .social{position:absolute;left:185px;top:68px;display:flex;gap:4px}
  .social i{display:block;width:10px;height:10px;background:#fff}
  .colour-band{position:absolute;left:0;bottom:0;width:100%;height:4px;
    background:linear-gradient(90deg,var(--sky) 0 33%,var(--leaf) 33% 66%,var(--flame) 66% 100%)}
</style>
</head>
<body>
<main class="stage">

  <!-- Bar chart slide -->
  <section class="slide" style="left:66px;top:199px">
    <h2 class="slide-title">OUR CHART</h2>
    <div class="title-rule"></div>
    <svg class="chart" width="446" height="345" viewBox="0 0 446 345">
      <g stroke="#333" stroke-width="1">
        <line x1="84" y1="66" x2="84" y2="222"/>
        <line x1="80" y1="66" x2="84" y2="66"/><line x1="80" y1="92" x2="84" y2="92"/>
        <line x1="80" y1="118" x2="84" y2="118"/><line x1="80" y1="144" x2="84" y2="144"/>
        <line x1="80" y1="170" x2="84" y2="170"/><line x1="80" y1="196" x2="84" y2="196"/>
        <line x1="80" y1="222" x2="84" y2="222"/>
      </g>
      <g>
        <rect x="94" y="110" width="15" height="112" fill="#0d96d4"/>
        <rect x="109" y="159" width="16" height="63" fill="#8cc040"/>
        <rect x="125" y="171" width="16" height="51" fill="#e9572f"/>
        <rect x="160" y="141" width="16" height="81" fill="#0d96d4"/>
        <rect x="176" y="110" width="16" height="112" fill="#8cc040"/>
        <rect x="192" y="171" width="15" height="51" fill="#e9572f"/>
        <rect x="227" y="120" width="16" height="102" fill="#0d96d4"/>
        <rect x="243" y="173" width="16" height="49" fill="#8cc040"/>
        <rect x="259" y="151" width="15" height="71" fill="#e9572f"/>
        <rect x="294" y="124" width="16" height="98" fill="#0d96d4"/>
        <rect x="310" y="162" width="15" height="60" fill="#8cc040"/>
        <rect x="325" y="114" width="16" height="108" fill="#e9572f"/>
      </g>
      <text class="year" x="118" y="245" text-anchor="middle">2009</text>
      <text class="year" x="185" y="245" text-anchor="middle">2010</text>
      <text class="year" x="251" y="245" text-anchor="middle">2011</text>
      <text class="year" x="318" y="245" text-anchor="middle">2012</text>
    </svg>
    <div class="legend" style="left:59px">
      <div class="legend-head"><i style="background:var(--sky)"></i>LOREM IPSUM</div>
      <p>Lorem ipsum dolor sit amet, consectetur adipiscing elit, sed do eiusmod tempor incididunt ut labore et dolore magna</p>
    </div>
    <div class="legend" style="left:183px">
      <div class="legend-head"><i style="background:var(--leaf)"></i>LOREM IPSUM</div>
      <p>Lorem ipsum dolor sit amet, consectetur adipiscing elit, sed do eiusmod tempor incididunt ut labore et dolore magna</p>
    </div>
    <div class="legend" style="left:303px">
      <div class="legend-head"><i style="background:var(--flame)"></i>LOREM IPSUM</div>
      <p>Lorem ipsum dolor sit amet, consectetur adipiscing elit, sed do eiusmod tempor incididunt ut labore et dolore magna</p>
    </div>
    <div class="brand brand-small"><span class="dot"></span>lanternis</div>
    <div class="slide-footer"><span class="page-no">2</span></div>
  </section>

  <!-- Donut statistics slide -->
  <section class="slide" style="left:528px;top:199px">
    <h2 class="slide-title">OUR CHART</h2>
    <div class="title-rule"></div>

    <div class="stat" style="left:31px">
      <svg width="70" height="70" viewBox="0 0 70 70">
        <g fill="none" stroke-width="7">
          <circle cx="35" cy="35" r="30" pathLength="100" stroke="#8cc040" stroke-dasharray="17 83" stroke-dashoffset="-75"/>
          <circle cx="35" cy="35" r="30" pathLength="100" stroke="#e9572f" stroke-dasharray="21 79" stroke-dashoffset="-93"/>
          <circle cx="35" cy="35" r="30" pathLength="100" stroke="#0d96d4" stroke-dasharray="59 41" stroke-dashoffset="-15"/>
        </g>
        <g fill="#6b6f78">
          <circle cx="31" cy="30" r="5"/><path d="M22 45c0-6 4-9 9-9s9 3 9 9z"/>
          <circle cx="41" cy="31" r="4"/><path d="M36 44c1-5 3-7 6-7s7 2 7 7z"/>
        </g>
      </svg>
      <div class="stat-value">76%</div>
      <p>Dolor sit amet, consectetur adipiscing elit, sed do eiusmod tempor incididunt ut labore et dolore magna aliqua. Ut enim ad minim veniam, quis nostrud exercitation ullamco laboris nisi ut aliquip ex ea cesse cillum dolore eu fugiat nulla pariatur.</p>
    </div>

    <div class="stat" style="left:169px">
      <svg width="70" height="70" viewBox="0 0 70 70">
        <g fill="none" stroke-width="7">
          <circle cx="35" cy="35" r="30" pathLength="100" stroke="#e9572f" stroke-dasharray="22 78" stroke-dashoffset="-77"/>
          <circle cx="35" cy="35" r="30" pathLength="100" stroke="#0d96d4" stroke-dasharray="49 51" stroke-dashoffset="0"/>
          <circle cx="35" cy="35" r="30" pathLength="100" stroke="#8cc040" stroke-dasharray="26 74" stroke-dashoffset="-50"/>
        </g>
        <circle cx="35" cy="35" r="10" fill="none" stroke="#6b6f78" stroke-width="6" stroke-dasharray="3.2 2"/>
        <circle cx="35" cy="35" r="8" fill="#6b6f78"/>
        <circle cx="35" cy="35" r="3.5" fill="#fff"/>
      </svg>
      <div class="stat-value">45%</div>
      <p>Dolor sit amet, consectetur adipiscing elit, sed do eiusmod tempor incididunt ut labore et dolore magna aliqua. Ut enim ad minim veniam, quis nostrud exercitation ullamco laboris nisi ut aliquip ex ea cesse cillum dolore eu fugiat nulla pariatur.</p>
    </div>

    <div class="stat" style="left:319px">
      <svg width="70" height="70" viewBox="0 0 70 70">
        <g fill="none" stroke-width="7">
          <circle cx="35" cy="35" r="30" pathLength="100" stroke="#8cc040" stroke-dasharray="49 51" stroke-dashoffset="-50"/>
          <circle cx="35" cy="35" r="30" pathLength="100" stroke="#e9572f" stroke-dasharray="21 79" stroke-dashoffset="0"/>
          <circle cx="35" cy="35" r="30" pathLength="100" stroke="#0d96d4" stroke-dasharray="27 73" stroke-dashoffset="-22"/>
        </g>
        <g fill="#6b6f78">
          <rect x="24" y="37" width="6" height="9"/><rect x="32" y="33" width="6" height="13"/><rect x="40" y="29" width="6" height="17"/>
          <path d="M22 34l12-10 4 3 6-5-2-2h7v7l-2-2-9 7-4-3-10 8z"/>
        </g>
      </svg>
      <div class="stat-value">20%</div>
      <p>Dolor sit amet, consectetur adipiscing elit, sed do eiusmod tempor incididunt ut labore et dolore magna aliqua. Ut enim ad minim veniam, quis nostrud exercitation ullamco laboris nisi ut aliquip ex ea cesse cillum dolore eu fugiat nulla pariatur.</p>
    </div>

    <div class="brand brand-small"><span class="dot"></span>lanternis</div>
    <div class="slide-footer"><span class="page-no">2</span></div>
  </section>

  <!-- Two column text slide -->
  <section class="slide" style="left:986px;top:199px">
    <h2 class="slide-title">TWO COLOUM</h2>
    <div class="title-rule"></div>
    <div class="col" style="left:37px">
      <p>Lorem ipsum dolor sit amet, consectetur adipisc-ing elit, sed do eiusmod tempor incididunt ut labore et dolore magna aliqua. Ut enim ad minim veniam, quis nostrud exercitation ullamco laboris nisi ut aliquip ex ea commodo consequat. Duis aute irure dolor in reprehenderit in voluptate velit esse cillum dolore eu fugiat nulla pariatur. dolore eu fugiat nulla pariatur dolore eu fugiat nulla pariatur. .</p>
      <p>Lorem ipsum dolor sit amet, consectetur adipisc-ing elit, sed do eiusmod tempor incididunt ut labore et dolore magna aliqua. Ut enim ad minim veniam, quis nostrud exercitation ullamco laboris</p>
    </div>
    <div class="col" style="left:240px">
      <p>Lorem ipsum dolor sit amet, consectetur adipisc-ing elit, sed do eiusmod tempor incididunt ut labore et dolore magna aliqua. Ut enim ad minim veniam, quis nostrud exercitation ullamco laboris nisi ut aliquip ex ea commodo consequat. Duis aute irure dolor in reprehenderit in voluptate velit esse cillum dolore eu fugiat nulla pariatur. dolore eu fugiat nulla pariatur dolore eu fugiat nulla pariatur. .</p>
      <p>Lorem ipsum dolor sit amet, consectetur adipisc-ing elit, sed do eiusmod tempor incididunt ut labore et dolore magna aliqua. Ut enim ad minim veniam, quis nostrud exercitation ullamco laboris</p>
    </div>
    <div class="brand brand-small"><span class="dot"></span>lanternis</div>
    <div class="slide-footer"><span class="page-no">2</span></div>
  </section>

  <!-- Image and text slide -->
  <section class="slide dark" style="left:66px;top:563px">
    <h2 class="panel-title">IMAGE &amp; TEXT</h2>
    <h3 class="panel-sub">LOREM IPSUM DOLOR SIT MET</h3>
    <p class="panel-text">Lorem ipsum dolor sit amet, consectetur adipisc-ing elit, sed do eiusmod tempor incididunt ut labore et dolore magna aliqua. Ut enim ad minim veniam, quis nostrud exercitation ullamco laboris nisi ut aliquip ex ea commodo consequat. Duis aute irure dolor in reprehenderit in voluptate velit esse cillum dolore eu fugiat nulla pariatur.</p>
    <div class="photo-portrait" role="img" aria-label="Black and white photo of a smiling woman and man in business clothes"></div>
    <div class="brand brand-small brand-light"><span class="dot"></span>lanternis</div>
  </section>

  <!-- Section title slide -->
  <section class="slide" style="left:528px;top:563px">
    <div class="photo-team" role="img" aria-label="Team of business people in suits, toned dark blue"></div>
    <div class="section">
      <svg width="58" height="58" viewBox="0 0 58 58">
        <circle cx="29" cy="29" r="28" fill="#0d96d4"/>
        <circle cx="32" cy="15" r="4.5" fill="#fff"/>
        <path d="M22 25h12l-5 17c-.5 2 1 2.5 4-1l1 1.5c-4 5-8 6-11 5-2-1-2-3-1.5-5l3.5-12h-3z" fill="#fff"/>
      </svg>
      <div class="section-rule"></div>
      <h2 class="section-title">SECTION TITLE</h2>
    </div>
  </section>

  <!-- Contact slide -->
  <section class="slide" style="left:986px;top:565px;height:343px">
    <div class="brand brand-large"><span class="dot"></span>lanternis</div>
    <div class="map" role="img" aria-label="Street map of the Antwerp office location with a red pin"></div>
    <div class="contact">
      <div class="contact-item" style="left:55px;top:26px"><span class="ico"></span><span>Lanternis Group bvba<br>Ravelstraat 12 bus 4<br>2000 Antwerpen | Belgium</span></div>
      <div class="contact-item" style="left:185px;top:28px"><span class="ico"></span><span>www.lanternis-group.eu</span></div>
      <div class="contact-item" style="left:55px;top:68px"><span class="ico"></span><span>info@lanternis-group.eu</span></div>
      <div class="social"><i></i><i></i><i></i></div>
    </div>
    <div class="colour-band"></div>
  </section>

</main>
</body>
</html>
```